Need Business Card for our Real Estate Business with Sales Executive's Picture

PANTONE 484 C ( RED)

PANTONE 2766 C ( BLUE

Industry/Entity Type

Real Estate

Contact Information for Business Card

Name, Mobile, email, & picture of Person
Agency Phone, address, Web address

Requirements
Must have
• Our Logo Colours, Agent Picture,

```html
<!DOCTYPE html>
<html lang="en">
<head>
<meta charset="utf-8">
<title>Meridan Realty — Business Card</title>
<link rel="stylesheet" href="https://fonts.googleapis.com/css2?family=Cinzel:wght@400;600&family=Crimson+Text:wght@400;600&display=swap">
<style>
  :root {
    --navy: #0d1640;
    --brand-red: #7a1b24;
    --role-red: #b03a46;
    --white: #ffffff;
    --paper: #ffffff;
    --stage: #2b2b2e;
    --suit-blue: #2a3f8f;
    --suit-light: #dfe4f2;
  }
  * { box-sizing: border-box; margin: 0; padding: 0; }
  html, body { width: 1200px; height: 880px; overflow: hidden; }
  body {
    background: var(--stage);
    font-family: "Crimson Text", Georgia, serif;
    position: relative;
  }
  .card {
    position: absolute;
    left: 250px;
    width: 700px;
    height: 400px;
    border-radius: 26px;
    overflow: hidden;
  }
  .card--back { top: 20px; background: var(--navy); }
  .card--front { top: 460px; background: var(--paper); }

  .wordmark {
    font-family: "Cinzel", "Times New Roman", serif;
    font-weight: 600;
    display: flex;
    align-items: center;
    gap: 14px;
    white-space: nowrap;
  }
  .wordmark__dot { width: 12px; height: 12px; background: var(--brand-red); flex: none; }

  .card--back .wordmark {
    position: absolute; top: 140px; left: 0; right: 0;
    justify-content: center; color: var(--white); font-size: 52px; letter-spacing: 4px;
  }
  .card--back .rule {
    position: absolute; top: 220px; left: 200px; width: 300px;
    height: 1px; background: var(--white);
  }
  .card--back .web {
    position: absolute; top: 268px; left: 0; right: 0; text-align: center;
    color: var(--white); font-size: 17px; letter-spacing: 4px;
  }

  .agent-photo {
    position: absolute; left: 470px; top: 24px; width: 220px; height: 290px;
    background: linear-gradient(180deg, var(--suit-light) 0%, #7d8fc7 45%, var(--suit-blue) 100%);
    border-radius: 6px 6px 0 0;
  }
  .card__wave { position: absolute; inset: 0; width: 700px; height: 400px; }
  .card--front .wordmark {
    position: absolute; top: 122px; left: 70px; color: var(--navy);
    font-size: 30px; letter-spacing: 3px;
  }
  .card--front .rule {
    position: absolute; top: 172px; left: 70px; width: 300px; height: 1px; background: var(--navy);
  }
  .contact { position: absolute; left: 44px; top: 266px; color: var(--white); }
  .contact__name {
    font-family: "Cinzel", "Times New Roman", serif; font-size: 21px; letter-spacing: 1px;
    padding-bottom: 4px; border-bottom: 1px solid var(--white); width: 290px; white-space: nowrap;
  }
  .contact__role { font-family: "Crimson Text", Georgia, serif; color: var(--role-red); font-size: 17px; }
  .contact__line { font-size: 17px; line-height: 22px; }
  .contact__line:first-of-type { margin-top: 6px; }
  .icon-row { display: flex; align-items: center; gap: 8px; font-size: 17px; }
  .icon-row svg { width: 20px; height: 20px; flex: none; }
  .contact__phone { margin-top: 6px; }
  .contact__email { position: absolute; left: 380px; top: 322px; color: var(--white); }
</style>
</head>
<body>

<section class="card card--back" aria-label="Card back">
  <div class="wordmark"><span class="wordmark__dot"></span>MERIDAN REALTY</div>
  <div class="rule"></div>
  <p class="web">www.meridanrealty.com</p>
</section>

<section class="card card--front" aria-label="Card front">
  <div class="agent-photo" role="img" aria-label="Portrait photo of the sales agent in a blue suit"></div>
  <svg class="card__wave" viewBox="0 0 700 400" aria-hidden="true">
    <path d="M0,200 C150,265 300,232 470,190 S640,150 700,145 L700,400 L0,400Z" fill="var(--navy)"/>
    <path d="M150,236 C280,242 370,214 480,184 S650,150 700,146" fill="none" stroke="var(--brand-red)" stroke-width="7"/>
    <path d="M160,246 C290,252 380,224 490,194 S660,160 700,158" fill="none" stroke="var(--white)" stroke-width="3"/>
  </svg>

  <div class="wordmark"><span class="wordmark__dot"></span>MERIDAN REALTY</div>
  <div class="rule"></div>

  <div class="contact">
    <p class="contact__name">DANIEL BROOKS <span class="contact__role">| Owner</span></p>
    <p class="contact__line">PO Box 480 Harbour Road</p>
    <p class="contact__line">Level 2, Northgate</p>
    <p class="icon-row contact__phone">
      <svg viewBox="0 0 20 20"><circle cx="10" cy="10" r="10" fill="var(--brand-red)"/><rect x="7" y="4.5" width="6" height="11" rx="1.2" fill="none" stroke="#fff" stroke-width="1.4"/></svg>
      (555) 014-2290
    </p>
  </div>
  <p class="icon-row contact__email">
    <svg viewBox="0 0 20 20"><circle cx="10" cy="10" r="10" fill="var(--brand-red)"/><rect x="5" y="6.5" width="10" height="7" fill="#fff"/><path d="M5,6.5 L10,10.5 L15,6.5" fill="none" stroke="var(--brand-red)" stroke-width="1.2"/></svg>
    info@meridanrealty.com
  </p>
</section>

</body>
</html>
```